Event flyer for Sunday night Youth Group

Need a 4 x 6 or 5 x 7 flyer for a new youth group starting on April 14. The youth group is for students in middle school and high school so it needs to look fun and cool, but not childish. I prefer it not to include pictures of people unless it's so obscure you can't really see their faces. I've uploaded some pictures of flyers I like. I've also attached a couple versions of our logo to use on the flyer.
Information the flyer needs to include:
Youth Group
Sundays, 6-8pm (beginning April 14)
Location: Merriwick's - 4219 Hollowfern Ln S, Keizer, 97418
There will be dinner, games, friends, and a message.
Target Market(s)
Youth ages 13-18
Industry/Entity Type
Church
Colors
Designer to choose colors to be used in the design.
Look and feel

```html
<!DOCTYPE html>
<html lang="en">
<head>
<meta charset="utf-8">
<title>Youth Group Flyer</title>
<link href="https://fonts.googleapis.com/css2?family=Oswald:wght@500;700&family=Montserrat:wght@500&display=swap" rel="stylesheet">
<style>
  :root {
    --navy: #043047;
    --green: #6f9e6d;
    --white: #ffffff;
    --backdrop: #d4d4d4;
  }
  html, body {
    margin: 0;
    width: 1200px;
    height: 1076px;
    overflow: hidden;
    background: var(--backdrop);
  }
  .flyer {
    position: absolute;
    left: 239px;
    top: 33px;
    width: 722px;
    height: 1010px;
    display: block;
  }
  .headline { font-family: "Oswald", sans-serif; font-weight: 700; fill: var(--navy); }
  .info-title { font-family: "Oswald", sans-serif; font-weight: 700; fill: var(--white); }
  .info-sub { font-family: "Oswald", sans-serif; font-weight: 500; fill: var(--white); }
  .info-time { font-family: "Montserrat", sans-serif; font-weight: 500; fill: var(--white); }
  .address { font-family: "Montserrat", sans-serif; font-weight: 500; fill: var(--white); font-size: 27px; }
  .brand-name { font-family: "Montserrat", sans-serif; font-weight: 500; fill: var(--navy); }
  .perks { font-family: "Oswald", sans-serif; font-weight: 500; fill: var(--navy); }
</style>
</head>
<body>
<svg class="flyer" viewBox="0 0 1068 1495" xmlns="http://www.w3.org/2000/svg">
  <!-- base -->
  <rect class="flyer-base" width="1068" height="1495" fill="var(--green)"/>

  <!-- white header with torn edge -->
  <path class="header-band" fill="var(--white)" d="M0 0 H1068 V307 L1048 310 1030 308 1008 303 985 306 960 300 935 304 918 310 900 312 880 308 860 310 840 306 820 308 800 302 780 306 760 310 740 312 720 316 700 318 680 324 660 326 640 332 620 330 600 334 580 338 560 336 540 338 520 340 500 336 480 338 460 344 440 342 420 346 400 344 380 340 360 334 340 326 320 330 300 328 280 332 260 338 240 336 220 338 200 340 180 346 160 350 140 356 120 360 100 366 80 372 60 374 40 370 20 364 0 362 Z"/>

  <!-- navy info band with torn edges -->
  <path class="info-band" fill="var(--navy)" d="M0 905 L20 902 40 900 60 904 80 902 100 900 120 898 140 896 160 894 180 898 200 896 220 894 240 892 260 894 280 890 300 886 320 884 340 882 360 880 380 876 400 872 420 874 440 870 460 866 480 864 500 864 520 862 540 866 560 870 580 874 600 872 620 870 640 874 660 870 680 866 700 864 720 866 740 862 760 860 780 858 800 856 820 852 840 848 860 846 880 842 900 838 920 836 940 834 960 838 980 842 1000 846 1020 848 1040 850 1068 848 V1270 L1048 1268 1030 1272 1010 1274 990 1278 970 1276 950 1270 930 1266 910 1262 890 1256 870 1252 850 1248 830 1250 810 1252 790 1248 770 1244 750 1240 730 1236 710 1234 690 1232 670 1234 650 1236 630 1234 610 1232 590 1236 570 1238 550 1236 530 1240 510 1238 490 1236 470 1234 450 1228 430 1224 410 1222 390 1220 370 1222 350 1218 330 1214 310 1212 290 1214 270 1210 250 1212 230 1208 210 1210 190 1212 170 1208 150 1210 130 1212 110 1214 90 1212 70 1214 50 1216 30 1218 10 1220 0 1220 Z"/>

  <!-- organisation name -->
  <g class="brand">
    <rect class="brand-mark" x="230" y="135" width="90" height="90" fill="var(--green)"/>
    <text class="brand-name" x="393" y="188" font-size="64" textLength="475" lengthAdjust="spacingAndGlyphs">WAYMARK</text>
    <text class="brand-name" x="460" y="233" font-size="34" textLength="340" lengthAdjust="spacing">FELLOWSHIP</text>
  </g>

  <!-- headline -->
  <text class="headline" x="302" y="573" font-size="270" textLength="465" lengthAdjust="spacingAndGlyphs">YOUTH</text>
  <text class="headline" x="296" y="818" font-size="270" textLength="476" lengthAdjust="spacingAndGlyphs">GROUP</text>

  <!-- schedule -->
  <g class="schedule">
    <text class="info-title" x="116" y="1012" font-size="118" textLength="282" lengthAdjust="spacingAndGlyphs">SUNDAYS</text>
    <text class="info-time" x="116" y="1062" font-size="48" textLength="282" lengthAdjust="spacing">6PM-8PM</text>
    <text class="info-sub" x="116" y="1108" font-size="52" textLength="282" lengthAdjust="spacingAndGlyphs">BEGINNING APRIL 14</text>
  </g>

  <rect class="info-divider" x="530" y="888" width="8" height="284" fill="var(--white)"/>

  <!-- location -->
  <g class="location">
    <text class="info-title" x="604" y="1012" font-size="118" textLength="310" lengthAdjust="spacingAndGlyphs">LOCATION:</text>
    <text class="address" x="604" y="1046">MERRIWICK'S</text>
    <text class="address" x="604" y="1086">4219 HOLLOWFERN LN S</text>
    <text class="address" x="604" y="1127">KEIZER</text>
    <text class="address" x="604" y="1168">97418</text>
  </g>

  <!-- what to expect -->
  <g class="perks-box">
    <path d="M273 1320 H433 M635 1320 H794 V1403 H273 V1320" fill="none" stroke="var(--navy)" stroke-width="4"/>
    <text class="perks" x="534" y="1338" text-anchor="middle" font-size="44" textLength="164" lengthAdjust="spacingAndGlyphs">THERE WILL BE</text>
    <text class="perks" x="534" y="1384" text-anchor="middle" font-size="44" textLength="480" lengthAdjust="spacingAndGlyphs">DINNER, GAMES, FRIENDS, AND A MESSAGE.</text>
  </g>
</svg>
</body>
</html>
```